Verdalunex webpage design

We are offering eco/sustainable theme vacations and make them bookable via our site. Our reference site is www.hovkalume.com. We want something similar but with a bit more creativity and elegant design. In our colors, which would depend on our logo colors.

NB: WE ARE NOT ASKING FOR A FULL BLOWN SITE. WE NEED 2 PAGE DESIGN FOR THE FIRST IMPRESSION. AFTER THAT WE CREATE A BUDGET FOR COMPLETION OF THE PROJECT.

Target Market(s)

Eco/Sustainable tourism.

Industry/Entity Type

Tourism

Coding

Coded - Design and coding required

Number of Pages Required

2 page

Requirements
Must have
• Reference site is hovkalume.com. But be creative and design something a bit different and more beautiful.
• NB: WE ARE NOT ASKING FOR A FULL BLOWN SITE. WE NEED 2 PAGE DESIGN FOR THE FIRST IMPRESSION. AFTER THAT WE CREATE A BUDGET FOR COMPLETION OF THE PROJECT.
• Please see our logo.

```html
<!DOCTYPE html>
<html lang="en">
<head>
<meta charset="utf-8">
<title>Verdalunex – Experience History</title>
<link href="https://fonts.googleapis.com/css2?family=Playfair+Display:ital,wght@1,700;1,900&family=Roboto:wght@400;500;700&display=swap" rel="stylesheet">
<style>
:root{
  --blue:#16a9ec;
  --green:#2fd58b;
  --ink:#333;
  --muted:#777;
  --line:#e2e2e2;
  --card:#f2f2f2;
  --footer:#333335;
  --footer-text:#a9a9a9;
  --star:#f6b51c;
}
*{margin:0;padding:0;box-sizing:border-box}
html,body{width:715px;height:1200px;overflow:hidden;background:#fff}
body{position:relative;font-family:'Roboto',sans-serif;color:var(--ink)}
.abs{position:absolute}
.grad{background:linear-gradient(90deg,var(--blue),var(--green))}

/* header */
.topbar{left:0;top:0;width:715px;height:24px;background:#fff}
.brand{display:flex;align-items:center;gap:3px;font-weight:700;font-size:11px;color:#222}
.brand .dot{width:10px;height:10px;border-radius:50%;background:var(--blue)}
.nav a{position:absolute;top:8px;font-size:7px;color:#444;text-decoration:none;white-space:nowrap}
.signup{left:522px;top:4px;width:54px;height:15px;border-radius:8px;color:#fff;font-size:7px;display:flex;align-items:center;justify-content:center;gap:3px}

/* hero */
.hero{left:0;top:24px;width:715px;height:378px;background:linear-gradient(180deg,#4f6640 0%,#6b6552 30%,#5d554b 60%,#7a6f62 100%)}
.hero-shade{left:0;top:24px;width:715px;height:378px;background:rgba(0,0,0,.18)}
.hero-title{left:0;top:168px;width:715px;text-align:center;font-family:'Playfair Display',serif;font-style:italic;font-weight:900;font-size:31px;color:#fff}
.hero-sub{left:0;top:210px;width:715px;text-align:center;font-size:8px;color:#fff}
.hero-btn{left:320px;top:234px;width:74px;height:20px;border-radius:10px;color:#fff;font-size:8px;display:flex;align-items:center;justify-content:center}

/* filters */
.fh{left:150px;font-size:7px;font-weight:500;color:#333}
.reset{left:150px;top:448px;font-size:5px;color:#777}
.tag{height:15px;display:flex;align-items:center;justify-content:center;font-size:6.5px;color:#fff;background:var(--blue)}
.tag.off{background:#fff;border:1px solid #ddd;color:#aaa}
.seemore{font-size:5px;color:#777}
.track{left:150px;width:112px;height:2px;background:#ddd}
.fill{height:2px;width:72px;background:linear-gradient(90deg,var(--blue),var(--green))}
.knob{width:6px;height:6px;border-radius:50%;top:-2px}
.lbl{font-size:6px;color:#777}
.months{left:150px;top:646px;width:112px;display:grid;grid-template-columns:repeat(6,1fr);gap:1px}
.months span{height:14px;display:flex;align-items:center;justify-content:center;font-size:6px;color:#fff;background:#d6d6d6}
.months span.on{background:var(--blue)}
.dest{left:151px;top:702px;width:111px;height:15px;border:1px solid #ddd;display:flex;align-items:center;gap:4px;padding-left:5px;font-size:6.5px;color:#999}
.opt{left:150px;display:flex;align-items:center;gap:4px;font-size:6px;color:#777}
.radio{width:8px;height:8px;border-radius:50%;border:1px solid #bbb;position:relative}
.radio.on{border-color:var(--green)}
.radio.on::after{content:"";position:absolute;left:1.5px;top:1.5px;width:3px;height:3px;border-radius:50%;background:var(--green)}

/* tour cards */
.tour{left:289px;width:272px;height:97px;background:var(--card)}
.tour .photo{position:absolute;left:0;top:0;width:108px;height:97px}
.tour .name{position:absolute;left:116px;top:7px;font-family:'Playfair Display',serif;font-style:italic;font-weight:700;font-size:8.5px;color:#222}
.tour .price{position:absolute;right:9px;top:7px;text-align:right;font-size:8px;color:#666;line-height:1}
.tour .price small{display:block;font-size:4.5px;margin-top:1px}
.tour .stars{position:absolute;left:116px;top:21px;font-size:7px;letter-spacing:.5px;color:var(--star)}
.tour .stars .e{color:#bbb}
.tour .meta{position:absolute;left:116px;font-size:4.8px;color:#555;display:flex;gap:3px;line-height:1.3}
.tour .meta b{font-weight:500;color:#333}
.tour .feats{position:absolute;left:116px;top:81px;display:flex;gap:5px;font-size:5px;color:var(--green)}
.tour .details{position:absolute;left:194px;top:74px;width:30px;height:15px;border:1px solid #ccc;font-size:5px;color:#999;display:flex;align-items:center;justify-content:center}
.tour .book{position:absolute;left:228px;top:74px;width:36px;height:15px;font-size:5px;font-weight:700;color:#fff;display:flex;align-items:center;justify-content:center}
.heart{position:absolute;left:8px;top:8px}

/* footer */
.footer{left:0;top:999px;width:715px;height:201px;background:var(--footer)}
.footer .brand{color:#fff}
.ftxt{font-size:6.5px;line-height:10.4px;color:var(--footer-text)}
.fhd{font-size:7.5px;font-weight:700;color:#fff}
.soc{width:17px;height:17px;border-radius:50%;background:#6a6a6c}
.divider{left:139px;top:1142px;width:437px;height:1px;background:#666}
</style>
</head>
<body>

<header class="abs topbar">
  <div class="abs brand" style="left:139px;top:6px"><span class="dot"></span>Verdalunex</div>
  <nav class="nav">
    <a style="left:306px">Tours</a>
    <a style="left:341px">⌄ USD</a>
    <a style="left:383px">♡ Favorites</a>
    <a style="left:441px">Partners</a>
    <a style="left:485px">Log in</a>
  </nav>
  <div class="abs signup grad">
    <svg width="6" height="6" viewBox="0 0 10 10" fill="none" stroke="#fff" stroke-width="1.2"><circle cx="5" cy="3" r="2.2"/><path d="M1 10c0-3 2-4 4-4s4 1 4 4"/></svg>Sign up
  </div>
</header>

<section>
  <div class="abs hero" role="img" aria-label="Backpacker walking towards an ancient stone temple gate overgrown with trees"></div>
  <div class="abs hero-shade"></div>
  <h1 class="abs hero-title">Experience History</h1>
  <p class="abs hero-sub">Visiting protected areas intended as low impact and environmentally sustainable.</p>
  <div class="abs hero-btn grad">Book a Tour</div>
</section>

<aside>
  <div class="abs fh" style="top:433px">What are your interests?</div>
  <div class="abs reset">× Reset All</div>
  <div class="abs tag" style="left:150px;top:459px;width:33px">Outdoor</div>
  <div class="abs tag" style="left:187px;top:459px;width:20px">Art</div>
  <div class="abs tag off" style="left:211px;top:459px;width:34px">Nightlife</div>
  <div class="abs tag" style="left:150px;top:478px;width:28px">Music</div>
  <div class="abs tag" style="left:183px;top:478px;width:51px">Entertainment</div>
  <div class="abs tag" style="left:150px;top:496px;width:30px">Sports</div>
  <div class="abs tag" style="left:184px;top:496px;width:25px">Food</div>
  <div class="abs seemore" style="left:213px;top:501px">See more</div>

  <div class="abs fh" style="top:525px">What’s your spend limit?</div>
  <div class="abs track" style="top:547px"><div class="fill"></div>
    <div class="abs knob" style="left:-2px;background:var(--blue)"></div>
    <div class="abs knob" style="left:69px;background:var(--green)"></div></div>
  <div class="abs lbl" style="left:150px;top:556px">$500</div>
  <div class="abs lbl" style="left:245px;top:556px">$4500</div>

  <div class="abs fh" style="top:578px">For how long will you travel?</div>
  <div class="abs track" style="top:599px"><div class="fill"></div>
    <div class="abs knob" style="left:-2px;background:var(--blue)"></div>
    <div class="abs knob" style="left:69px;background:var(--green)"></div></div>
  <div class="abs lbl" style="left:150px;top:608px">1 Night/2 Days</div>
  <div class="abs lbl" style="left:219px;top:608px">9 Night/10 Days</div>

  <div class="abs fh" style="top:630px">When is you trip?</div>
  <div class="abs months">
    <span>Jan</span><span class="on">Feb</span><span class="on">Mar</span><span class="on">Apr</span><span>May</span><span>Jun</span>
    <span>Jul</span><span>Aug</span><span>Sep</span><span>Oct</span><span>Nov</span><span>Dec</span>
  </div>

  <div class="abs fh" style="top:690px">What’s your destination?</div>
  <div class="abs dest">
    <svg width="6" height="7" viewBox="0 0 10 12" fill="none" stroke="#999" stroke-width="1.2"><path d="M5 11s4-4 4-6.5A4 4 0 0 0 1 4.5C1 7 5 11 5 11z"/><circle cx="5" cy="4.5" r="1.3"/></svg>Jakarta, Indonesia
  </div>

  <div class="abs fh" style="top:731px">What to include?</div>
  <div class="abs opt" style="top:746px"><span class="radio on"></span>Breakfast</div>
  <div class="abs opt" style="top:759px"><span class="radio"></span>Airport Transfer</div>
  <div class="abs opt" style="top:772px"><span class="radio"></span>Moto Rental</div>
  <div class="abs opt" style="top:784px"><span class="radio"></span>Car Rental</div>
  <div class="abs opt" style="top:797px"><span class="radio"></span>Insurance</div>
</aside>

<main>
  <article class="abs tour" style="top:430px">
    <div class="photo" role="img" aria-label="Hikers on a green grassy mountain ridge" style="background:linear-gradient(160deg,#dfe5e6,#8ea45a 50%,#4f6a2e)"></div>
    <h3 class="name">Kerala Tour Package</h3>
    <div class="price">$1654<small>/Pax</small></div>
    <div class="stars">★★★<span class="e">☆☆</span></div>
    <div class="meta" style="top:36px">▢ Duration: <b>5 Nights / 6 Days</b></div>
    <div class="meta" style="top:46px">◉ Starting from: <b>Munnar (2) &gt; Thekkadi (3) &gt; Allepey (2)</b></div>
    <div class="meta" style="top:56px">⚇ Max. Persons: <b>6 Pax</b></div>
    <div class="feats"><span>◎ Sightseeing</span><span>➤ Trekking</span></div>
    <div class="details">Details</div><div class="book grad">Book Now</div>
  </article>

  <article class="abs tour" style="top:537px">
    <div class="photo" role="img" aria-label="Lush green tropical hills under a cloudy sky" style="background:linear-gradient(170deg,#a9c6d6,#6f9a3d 45%,#355b22)"></div>
    <svg class="heart" width="8" height="7" viewBox="0 0 10 9"><path d="M5 9 1 5C-1 3 .5 0 3 .5 4 .7 5 2 5 2s1-1.3 2-1.5C9.5 0 11 3 9 5z" fill="#fff"/></svg>
    <h3 class="name">Dharamsala &amp; Dalhousie</h3>
    <div class="price">$2478<small>/Pax</small></div>
    <div class="stars">★★★★★</div>
    <div class="meta" style="top:36px">▢ Duration: <b>5 Nights / 6 Days</b></div>
    <div class="meta" style="top:46px">◉ Starting from: <b>Munnar (2) &gt; Thekkadi (3) &gt; Allepey (2)</b></div>
    <div class="meta" style="top:56px">⚇ Max. Persons: <b>6 Pax</b></div>
    <div class="feats"><span>◎ Sightseeing</span><span>ⓘ Guide</span></div>
    <div class="details">Details</div><div class="book grad">Book Now</div>
  </article>

  <article class="abs tour" style="top:644px">
    <div class="photo" role="img" aria-label="Split stone temple gate with mountain in the distance" style="background:linear-gradient(180deg,#7fb4dc,#6f7a6a 50%,#3f4a35)"></div>
    <svg class="heart" width="8" height="7" viewBox="0 0 10 9"><path d="M5 9 1 5C-1 3 .5 0 3 .5 4 .7 5 2 5 2s1-1.3 2-1.5C9.5 0 11 3 9 5z" fill="#fff"/></svg>
    <h3 class="name">Shimla &amp; Manali</h3>
    <div class="price">$3854<small>/Pax</small></div>
    <div class="stars">★★★<span class="e">☆☆</span></div>
    <div class="meta" style="top:36px">▢ Duration: <b>7 Nights / 8 Days</b></div>
    <div class="meta" style="top:46px">◉ <span>Starting from: <b>Kalpa (2) &gt; Spiti Vale (3)<br>&gt; Kaza Ridge (2) &gt; Spiti Vale (1)</b></span></div>
    <div class="meta" style="top:62px">⚇ Max. Persons: <b>6 Pax</b></div>
    <div class="feats"><span>◎ Boat Travel</span><span>➤ Trekking</span></div>
    <div class="details">Details</div><div class="book grad">Book Now</div>
  </article>

  <article class="abs tour" style="top:751px">
    <div class="photo" role="img" aria-label="Traveller at a mirror lake with snowy peaks" style="background:linear-gradient(180deg,#2b6f9c,#9fb8c6 45%,#3b5566 60%,#1b2c38)"></div>
    <svg class="heart" width="8" height="7" viewBox="0 0 10 9"><path d="M5 9 1 5C-1 3 .5 0 3 .5 4 .7 5 2 5 2s1-1.3 2-1.5C9.5 0 11 3 9 5z" fill="#2fd5b5"/></svg>
    <h3 class="name">Kerala Tour Package</h3>
    <div class="price">$1654<small>/Pax</small></div>
    <div class="stars">★★★★<span class="e">☆</span></div>
    <div class="meta" style="top:36px">▢ Duration: <b>5 Nights / 6 Days</b></div>
    <div class="meta" style="top:46px">◉ Starting from: <b>Munnar (2) &gt; Thekkadi (3) &gt; Allepey (2)</b></div>
    <div class="meta" style="top:56px">⚇ Max. Persons: <b>6 Pax</b></div>
    <div class="feats"><span>◎ Orientation</span><span>➤ Trekking</span></div>
    <div class="details">Details</div><div class="book grad">Book Now</div>
  </article>

  <article class="abs tour" style="top:858px">
    <div class="photo" role="img" aria-label="Traveller photographing sandstone arches" style="background:linear-gradient(160deg,#c9a97a,#e6dccb 45%,#9e8060 80%,#5b7fa0)"></div>
    <h3 class="name">Kerala Tour Package</h3>
    <div class="price">$1654<small>/Pax</small></div>
    <div class="stars">★★★<span class="e">☆☆</span></div>
    <div class="meta" style="top:36px">▢ Duration: <b>5 Nights / 6 Days</b></div>
    <div class="meta" style="top:46px">◉ Starting from: <b>Munnar (2) &gt; Thekkadi (3) &gt; Allepey (2)</b></div>
    <div class="meta" style="top:56px">⚇ Max. Persons: <b>6 Pax</b></div>
    <div class="feats"><span>◎ Sightseeing</span><span>➤ Trekking</span></div>
    <div class="details">Details</div><div class="book grad">Book Now</div>
  </article>
</main>

<footer class="abs footer">
  <div class="abs brand" style="left:139px;top:36px"><span class="dot"></span>Verdalunex</div>
  <p class="abs ftxt" style="left:139px;top:58px;width:135px">Lorem ipsum dolor sit amet, consectetuer adipiscing elit, sed diam nonummy nibh euismod tincidunt ut laoreet dolore magna aliquam erat volutpat.</p>
  <div class="abs" style="left:140px;top:114px;font-size:6.5px;color:#fff">FOLLOW US</div>
  <div class="abs soc" style="left:185px;top:110px"></div>
  <div class="abs soc" style="left:206px;top:110px"></div>
  <div class="abs soc" style="left:226px;top:110px"></div>
  <div class="abs soc" style="left:247px;top:110px"></div>

  <div class="abs fhd" style="left:313px;top:38px">SITEMAP</div>
  <div class="abs ftxt" style="left:313px;top:58px">Tours<br>Partners<br>Log In</div>

  <div class="abs fhd" style="left:388px;top:38px">CONTACT US</div>
  <div class="abs ftxt" style="left:389px;top:58px;width:10px">✆<br>✉<br>⌖</div>
  <div class="abs ftxt" style="left:400px;top:58px">+44 20 5550 1432<br>info@verdalunex.com<br>12 Fenwick Row,<br>Harlow Green, London<br>N7 4QT, UK</div>

  <div class="abs ftxt" style="left:139px;top:158px">Terms &amp; Conditions &nbsp;|&nbsp; Privacy Policy &nbsp;|&nbsp; Copyright © 2019 Verdalunex.</div>
</footer>
<div class="abs divider"></div>

</body>
</html>
```